Business cards design for T38 (Разработка визитных карточек)

We would like to get design of our business cards loosely based on our website design [url removed, login to view]

logo in vector is atteched

There should be following info to be present on business card:
Gavin Holcroft
CEO
T38
+7 (495) 804-27-63
+7 (495) 804-27-63
holcroft@tavimex-corp.com
128403, Moscow, Ulitsa Lipovaya, 7B

```html
<!DOCTYPE html>
<html lang="en">
<head>
<meta charset="utf-8">
<title>T38 Business Cards</title>
<link rel="stylesheet" href="https://fonts.googleapis.com/css2?family=Arimo:wght@400;700&display=swap">
<style>
  :root {
    --backdrop: #bcbcbc;
    --brand-red: #ff0000;
    --card-black: #000000;
    --ink-dark: #1a1a1a;
    --ink-light: #ffffff;
    --band-light: #ffffff;
  }
  * { margin: 0; padding: 0; box-sizing: border-box; }
  html, body {
    width: 1200px;
    height: 827px;
    overflow: hidden;
    background: var(--backdrop);
    font-family: "Arimo", Arial, sans-serif;
  }
  .canvas {
    position: relative;
    width: 1200px;
    height: 827px;
  }
  .card {
    position: absolute;
    top: 268px;
    width: 520px;
    height: 291px;
  }
  /* Back side */
  .card-back { left: 60px; }
  .card-back svg { position: absolute; inset: 0; }
  .card-back .brand-name {
    position: absolute;
    left: 150px;
    top: 92px;
    font-weight: 700;
    font-size: 100px;
    line-height: 1;
    color: var(--brand-red);
  }
  /* Front side */
  .card-front {
    left: 620px;
    background: var(--brand-red);
    clip-path: polygon(0 0, 498px 0, 520px 24px, 520px 267px, 498px 291px, 0 291px);
    color: var(--ink-light);
  }
  .logo-band {
    position: absolute;
    left: 0;
    top: 117px;
    width: 200px;
    height: 56px;
    background: linear-gradient(to right, var(--band-light) 0%, var(--band-light) 15%, var(--brand-red) 100%);
  }
  .card-front .brand-name {
    position: absolute;
    left: 14px;
    top: 118px;
    font-weight: 700;
    font-size: 56px;
    line-height: 1;
    color: var(--ink-dark);
  }
  .holder, .contacts, .online {
    position: absolute;
    right: 30px;
    text-align: right;
  }
  .holder { top: 34px; }
  .holder-name { font-size: 20px; line-height: 24px; color: var(--ink-dark); }
  .holder-role { font-size: 14px; line-height: 22px; }
  .contacts { top: 138px; font-size: 14px; line-height: 19.5px; font-weight: 700; font-style: normal; }
  .online { top: 245px; font-size: 14px; line-height: 19px; font-weight: 700; }
</style>
</head>
<body>
<main class="canvas">
  <section class="card card-back" aria-label="Card back">
    <svg width="520" height="291" viewBox="0 0 520 291">
      <polygon points="22,0 520,0 520,291 22,291 0,267 0,24" fill="var(--brand-red)"/>
      <polygon points="52,0 520,0 520,291 150,291 52,200" fill="var(--card-black)"/>
    </svg>
    <div class="brand-name">T38</div>
  </section>

  <section class="card card-front" aria-label="Card front">
    <div class="holder">
      <p class="holder-name">Gavin Holcroft</p>
      <p class="holder-role">CEO</p>
    </div>
    <div class="logo-band"></div>
    <div class="brand-name">T38</div>
    <address class="contacts">
      <p>+7 (495) 804-27-63</p>
      <p>+7 (495) 804-27-63</p>
      <p>128403, Moscow,</p>
      <p>Ulitsa Lipovaya, 7B</p>
    </address>
    <div class="online">
      <p>holcroft@tavimex-corp.com</p>
      <p>www.tavimex-corp.com</p>
    </div>
  </section>
</main>
</body>
</html>
```